Stationary Design (using existing logo)

Stationary (print and electronic version for Word/email), envelope, and fax cover. All companies are part of same family or course so designs can be the same, or essentially the same. Use the logos attached, same font and colors.

Target Market(s)

Real estate professionals. Investors and other property owners. Financial professionals.

Industry/Entity Type

Real Estate

Font styles to use
Serif

Requirements
Must have
• Should be a serious, sophisticated design in colors that match the business cards we uploaded. Design needs to match the color and fonts in the attached business cards. Can use the same design for each company, just change logo and color.
Should not have
• Nothing quirky or cute.

```html
<!DOCTYPE html>
<html lang="en">
<head>
<meta charset="utf-8">
<title>KRB Realty Partners Stationery</title>
<link href="https://fonts.googleapis.com/css2?family=EB+Garamond:wght@400;500&display=swap" rel="stylesheet">
<style>
  :root{
    --backdrop:#e6e1dc;
    --paper:#ffffff;
    --card-grey:#e9e9ea;
    --rust:#b1432a;
    --rust-dark:#9c3a22;
    --ink:#3a3633;
    --shadow:rgba(0,0,0,.12);
  }
  *{margin:0;padding:0;box-sizing:border-box}
  html,body{width:1200px;height:1070px;overflow:hidden}
  body{background:var(--backdrop);font-family:"EB Garamond",Georgia,serif;color:var(--ink);position:relative}
  .sheet{position:absolute;background:var(--paper);box-shadow:0 1px 3px var(--shadow);overflow:hidden}
  .brand-name{color:var(--rust);font-weight:500;letter-spacing:.06em;white-space:nowrap;line-height:1}
  .band{position:absolute;left:0;right:0;background:var(--rust);color:#fff;display:flex;align-items:center;font-size:8px;letter-spacing:.02em}
  .contact{font-size:7px;line-height:1.35}
  .contact .tag{color:var(--rust);margin-right:3px}

  /* letterhead */
  .letterhead{left:60px;top:39px;width:471px;height:666px}
  .letterhead .masthead{position:absolute;top:50px;left:0;right:0;text-align:center}
  .letterhead .brand-name{font-size:15px}
  .letterhead .contact{margin-top:8px}
  .letterhead .phones span{margin:0 6px}
  .letterhead .band{top:632px;height:34px;justify-content:center}

  /* business cards */
  .card{width:190px;height:111px;top:39px}
  .card-front{left:602px;background:var(--card-grey)}
  .card-front .brand-name{position:absolute;left:16px;bottom:18px;font-size:12px;color:#b9b4b0}
  .card-front .web{position:absolute;right:14px;top:54px;font-size:7px}
  .card-back{left:817px}
  .card-back .brand-name{position:absolute;top:44px;left:0;right:0;text-align:center;font-size:12px}
  .card-back .person{position:absolute;left:7px;top:74px;font-size:6px;line-height:1.25}
  .card-back .numbers{position:absolute;right:7px;top:74px;font-size:6px;line-height:1.25}
  .card-back .band{top:97px;height:14px;justify-content:center;font-size:7px}

  /* compliment slip */
  .slip{left:60px;top:737px;width:483px;height:235px}
  .slip .masthead{position:absolute;left:33px;top:52px}
  .slip .brand-name{font-size:13px}
  .slip .contact{margin-top:6px;font-size:6.5px}
  .slip .band{top:203px;height:32px;padding-left:33px;font-size:7.5px}

  /* envelope */
  .envelope{left:583px;top:737px;width:483px;height:291px;background:transparent;box-shadow:none}
  .envelope svg{position:absolute;left:0;top:0}
</style>
</head>
<body>

<section class="sheet letterhead">
  <header class="masthead">
    <div class="brand-name">KRB REALTY PARTNERS</div>
    <div class="contact">
      <div>www.krbrealty.com</div>
      <div>daniel@krbrealty.com</div>
      <div class="phones" style="margin-top:4px">
        <span><span class="tag">t</span>555.210.4400</span>
        <span><span class="tag">f</span>555.210.4401</span>
        <span><span class="tag">c</span>555.318.2207</span>
      </div>
    </div>
  </header>
  <footer class="band">1480 W Larkin Ave., Springfield, IL 62704</footer>
</section>

<section class="sheet card card-front">
  <div class="web">www.krbrealty.com</div>
  <div class="brand-name">KRB</div>
</section>

<section class="sheet card card-back">
  <div class="brand-name">KRB REALTY PARTNERS</div>
  <div class="person">Daniel Morris<br>Operations Director<br>daniel@krbrealty.com</div>
  <div class="numbers">555.210.4400<br>555.210.4401 (fax)<br>555.318.2207 (cell)</div>
  <footer class="band">1480 W Larkin Ave., Springfield, IL 62704</footer>
</section>

<section class="sheet slip">
  <header class="masthead">
    <div class="brand-name">KRB REALTY PARTNERS</div>
    <div class="contact">
      <div>www.krbrealty.com</div>
      <div style="margin-top:3px">daniel@krbrealty.com</div>
      <div style="margin-top:5px"><span class="tag">t</span>555.210.4400<br><span class="tag">f</span>555.210.4401<br><span class="tag">c</span>555.318.2207</div>
    </div>
  </header>
  <footer class="band">1480 W Larkin Ave., Springfield, IL 62704</footer>
</section>

<section class="sheet envelope">
  <svg width="483" height="291" viewBox="0 0 483 291" aria-hidden="true">
    <rect x="0" y="60" width="483" height="231" fill="#ffffff"/>
    <path d="M0 60 L24 10 Q30 0 42 0 L441 0 Q453 0 459 10 L483 60 Z" fill="#9c3a22"/>
    <path d="M0 60 L483 60 L420 122 Q414 128 404 128 L79 128 Q69 128 63 122 Z" fill="#b1432a"/>
  </svg>
</section>

</body>
</html>
```